Pinewharfs Vehicle Wrap Design for Vacation Rental Property Mgt Company

We are looking for a vehicle wrap design to extend our brand through our service vehicles. Design should be simple, professional, eye-catching, and incorporate our logo and corporate colors. Design should be flexible enough to be applied to a wide variety of trucks and cars. Not looking for FULL wrap, but rather separate graphics to be applied to white vehicles. Attached is ppt with a couple of our current vehicles and a few sample designs that has caught our attention. Copies of our current logo and biz card designs are also included.

Panels to include:
Logo (attached)
555-318-6249
www.Pinewharves.example
Vacation Rental Property Management
Property Maintenance Services
Linen & Laundry Services

Target Market(s)

Local adults 30-65

Industry/Entity Type

Font styles to use
Serif

Colors
0054AA
0677BA
7BADD7
CADEEF
E8F1F8

Requirements
Must have
• Logo, phone, web address, corporate colors,

```html
<!DOCTYPE html>
<html lang="en">
<head>
<meta charset="utf-8">
<title>Pinewharves Vehicle Wrap</title>
<link rel="stylesheet" href="https://fonts.googleapis.com/css2?family=Montserrat:wght@600&family=Oswald:wght@500&family=Roboto:ital,wght@1,700&display=swap">
<style>
  :root {
    --navy: #0b3a70;
    --sky: #1f9bda;
    --sky-soft: #3aa9e2;
    --white: #ffffff;
    --page: #e9e9ea;
  }
  html, body {
    margin: 0;
    padding: 0;
    width: 1200px;
    height: 627px;
    overflow: hidden;
    background: var(--page);
  }
  .wrap-art {
    display: block;
    width: 1200px;
    height: 627px;
  }
  .panel-base { fill: var(--white); }
  .swoosh-light { fill: var(--sky); }
  .brand-mark { fill: var(--navy); }
  .brand-name {
    font-family: "Montserrat", sans-serif;
    font-weight: 600;
    fill: var(--navy);
  }
  .brand-tagline {
    font-family: "Montserrat", sans-serif;
    font-weight: 600;
    fill: var(--navy);
    letter-spacing: 1px;
  }
  .headline {
    font-family: "Oswald", sans-serif;
    font-weight: 500;
    fill: var(--navy);
  }
  .phone {
    font-family: "Oswald", sans-serif;
    font-weight: 500;
    fill: var(--white);
  }
  .web {
    font-family: "Montserrat", sans-serif;
    font-weight: 600;
    fill: var(--sky-soft);
  }
  .service {
    font-family: "Roboto", sans-serif;
    font-style: italic;
    font-weight: 700;
    fill: var(--white);
  }
</style>
</head>
<body>
<svg class="wrap-art" viewBox="0 0 1200 627" xmlns="http://www.w3.org/2000/svg" role="img" aria-label="Pinewharves vehicle wrap layout">
  <defs>
    <linearGradient id="diagonal-fill" x1="1" y1="0" x2="0.35" y2="1">
      <stop offset="0" stop-color="#1f9bda"/>
      <stop offset="0.5" stop-color="#0d5fa6"/>
      <stop offset="1" stop-color="#0a3563"/>
    </linearGradient>
  </defs>

  <rect class="panel-base" x="0" y="0" width="1200" height="627"/>

  <path class="swoosh-light" d="M0 482 C 200 455, 420 425, 589 404 L 648 480 L 575 627 L 0 627 Z"/>

  <polygon fill="url(#diagonal-fill)" points="660,480 1200,70 1200,627 590,627"/>

  <g class="brand-lockup">
    <rect class="brand-mark" x="400" y="196" width="32" height="32"/>
    <text class="brand-name" x="444" y="225" font-size="38" textLength="240" lengthAdjust="spacingAndGlyphs">Pinewharves</text>
    <text class="brand-tagline" x="542" y="276" font-size="17" text-anchor="middle">VACATION</text>
    <text class="brand-tagline" x="542" y="297" font-size="17" text-anchor="middle">RENTALS</text>
  </g>

  <text class="headline" font-size="90" textLength="540" lengthAdjust="spacingAndGlyphs" transform="translate(640 462) rotate(-37)">PINEWHARVES</text>

  <text class="phone" x="890" y="359" font-size="54" textLength="255" lengthAdjust="spacingAndGlyphs">555-318-6249</text>
  <text class="web" x="986" y="386" font-size="14" textLength="155" lengthAdjust="spacingAndGlyphs">PINEWHARVES.EXAMPLE</text>

  <text class="service" font-size="13" text-anchor="end">
    <tspan x="579" y="429">Vacation</tspan>
    <tspan x="579" y="444">Rental Property</tspan>
    <tspan x="579" y="459">Management</tspan>
  </text>

  <text class="service" font-size="13" text-anchor="middle">
    <tspan x="867" y="393">Property Maintenance</tspan>
    <tspan x="867" y="408">Services</tspan>
  </text>

  <text class="service" font-size="13" text-anchor="middle">
    <tspan x="814" y="436">Linen &amp; Laundry</tspan>
    <tspan x="814" y="451">Services</tspan>
  </text>
</svg>
</body>
</html>
```